Business card for a plastic surgeon

i need a business card for a plastic surgeon. I have two adresses. The card should communicate safety, simmetry, beauty and with soft colors.
What i want in the card:
- my logo: Letters "R"and "B" (picture uploaded)
- my name: Renato Bastiani
- my registration: CRM 507 219
- my adresses and phone numbers (2):
- Av Dr Teixeira Lopes, 2710, sala 305 - Vila Olímpia | São Paulo/ SP - Phone: 11 4172-5036
- Al. Itapeva, 47, 3 andar - Alphaville | Barueri/ SP - Phone: 11 6350-2481

- my social network: site, facebook and instagram

Target Market(s)

people (95% girls and women) that want cosmetic procedures and plastic surgery

Industry/Entity Type

Business

Contact Information for Business Card

The card should communicate safety, simmetry, beauty and with soft colors.
Beige, brown, gray, rosy are some options. Color is free

Font styles to use
Serif

Requirements
Must have
• - my logo: Letters "R"and "B" (picture uploaded)
• - my name: Renato Bastiani
• - my registration: CRM 507 219
• - my adresses and phone numbers (2):
• - Av Dr Teixeira Lopes, 2710, sala 305 - Vila Olímpia | São Paulo/ SP - Phone: 11 4172-5036
• - Al. Itapeva, 47, 3 andar - Alphaville | Barueri/ SP - Phone: 11 6350-2481
• - my social network: site, facebook and instagram
Should not have
• other images (only my logo)

```html
<!DOCTYPE html>
<html lang="pt">
<head>
<meta charset="utf-8">
<title>Renato Bastiani – Cartão de visita</title>
<link href="https://fonts.googleapis.com/css2?family=Cinzel:wght@400&family=Open+Sans:wght@400&display=swap" rel="stylesheet">
<style>
  :root{
    --backdrop:#c8c8cc;
    --card-white:#ffffff;
    --ink:#2b2b2b;
    --ink-soft:#555555;
    --taupe:#a89580;
    --black:#0d0b0b;
    --rule:#6d6d6d;
  }
  *{margin:0;padding:0;box-sizing:border-box}
  html,body{width:1200px;height:1200px;overflow:hidden;background:var(--backdrop)}
  .stage{position:relative;width:1200px;height:1200px}
  .card{position:absolute;width:640px;height:370px;overflow:hidden;box-shadow:0 6px 18px rgba(0,0,0,.18)}
  .card--back{left:70px;top:150px;background:var(--black)}
  .card--front{left:490px;top:620px;background:var(--card-white)}

  .back-pattern{position:absolute;inset:0;background:var(--black)}
  .back-mark{position:absolute;left:0;right:0;top:160px;text-align:center;
    font-family:"Cinzel",serif;font-size:30px;letter-spacing:3px;color:var(--taupe)}
  .back-social{position:absolute;left:388px;top:288px;display:flex;gap:6px}
  .back-social span{width:12px;height:12px;background:var(--taupe);border-radius:2px}

  .identity{position:absolute;left:34px;top:112px}
  .identity__mark{width:14px;height:14px;border-radius:50%;background:var(--taupe);margin:0 0 10px 72px}
  .identity__name{font-family:"Cinzel",serif;font-size:21px;color:var(--ink);letter-spacing:.5px;white-space:nowrap}
  .identity__title{font-family:"Cinzel",serif;font-size:10.5px;letter-spacing:3.2px;color:var(--ink-soft);margin-top:2px}

  .rule{position:absolute;height:1px;background:var(--rule)}
  .rule--top{left:300px;top:118px;width:310px}
  .rule--contact{left:40px;top:232px;width:220px}

  .addresses{position:absolute;right:30px;top:130px;text-align:right;
    font-family:"Open Sans",sans-serif;font-size:12.5px;line-height:17px;color:var(--ink)}
  .addresses p+p{margin-top:6px}

  .contacts{position:absolute;left:40px;top:244px;list-style:none;
    font-family:"Open Sans",sans-serif;font-size:12.5px;line-height:19px;color:var(--ink)}
  .contacts li{display:flex;align-items:center;gap:8px}
  .contacts svg{width:11px;height:11px;fill:var(--taupe)}

  .footer-shape{position:absolute;left:0;top:0}
  .registration{position:absolute;right:24px;top:280px;font-family:"Open Sans",sans-serif;
    font-size:13px;color:var(--black)}
  .registration b{font-weight:400;color:#fff}
</style>
</head>
<body>
<main class="stage">
  <section class="card card--back" aria-label="Verso do cartão">
    <div class="back-pattern" role="img" aria-label="Padrão de fundo discreto com o monograma repetido"></div>
    <div class="back-mark">Renato Bastiani</div>
    <div class="back-social" aria-label="Redes sociais"><span></span><span></span></div>
  </section>

  <section class="card card--front" aria-label="Frente do cartão">
    <svg class="footer-shape" width="640" height="370" viewBox="0 0 640 370" aria-hidden="true">
      <polygon points="0,352 360,352 378,304 640,304 640,370 0,370" fill="var(--black)"/>
      <polygon points="378,274 640,274 640,304 368,304" fill="var(--taupe)"/>
    </svg>

    <div class="identity">
      <div class="identity__mark"></div>
      <div class="identity__name">DR. RENATO BASTIANI</div>
      <div class="identity__title">CIRURGIÃO PLÁSTICO</div>
    </div>

    <div class="rule rule--top"></div>
    <div class="addresses">
      <p>Al. Itapeva, 47, 3 andar -<br>Alphaville Barueri/ SP</p>
      <p>Av Dr Teixeira Lopes, 2710, sala<br>305 - Vila Olímpia São Paulo/ SP</p>
    </div>
    <div class="registration">registration: <b>CRM 507 219</b></div>

    <div class="rule rule--contact"></div>
    <ul class="contacts">
      <li><svg viewBox="0 0 24 24"><path d="M6.6 10.8a15.1 15.1 0 0 0 6.6 6.6l2.2-2.2a1 1 0 0 1 1-.25 11.4 11.4 0 0 0 3.6.57 1 1 0 0 1 1 1V20a1 1 0 0 1-1 1A17 17 0 0 1 3 4a1 1 0 0 1 1-1h3.5a1 1 0 0 1 1 1c0 1.25.2 2.45.57 3.57a1 1 0 0 1-.25 1z"/></svg>11 4172-5036</li>
      <li><svg viewBox="0 0 24 24"><path d="M6.6 10.8a15.1 15.1 0 0 0 6.6 6.6l2.2-2.2a1 1 0 0 1 1-.25 11.4 11.4 0 0 0 3.6.57 1 1 0 0 1 1 1V20a1 1 0 0 1-1 1A17 17 0 0 1 3 4a1 1 0 0 1 1-1h3.5a1 1 0 0 1 1 1c0 1.25.2 2.45.57 3.57a1 1 0 0 1-.25 1z"/></svg>11 6350-2481</li>
      <li><svg viewBox="0 0 24 24"><path d="M2 5h20v14H2z M2 5l10 8 10-8" /></svg>info@bastianiclinica.com</li>
      <li><svg viewBox="0 0 24 24"><circle cx="12" cy="12" r="10"/></svg>www.bastianiclinica.com</li>
    </ul>
  </section>
</main>
</body>
</html>
```